Brightwell cleaning and maintenance company

An expansive website whereby we can advertise our commercial cleaning and maintenance services across a service portfolio of commercial cleaning and property maintenance. Whereby potential skilled resources can deposit there resume so we can collaborate and match candidates to a broad range of cleaning and maintenance jobs/projects.
Updates

Looking for more extensive ideas so the front page can change pictures on it with the focus for Brightwell Commercial Cleaning and Maintenance. Also need to bring in all the portfolios we offer including 1. Equipment Cleaning and Sanitisation Services 2. High pressure gurney and play ground equipment cleaning 3. General Cleaning and Property Facilities Management 4. Project and Recruiting Services, to allow for potential professional cleaners, handy man, mechanics, warehousing resources , electricians to deposit there resume. Most of the designers have stuck with the old portfolio categories , however the portfolio of services we offer has been updated so that needs to be reflected in the website. Also not necessary to use all my original photos I would like the opening page of the website to perhaps be able to change and have different pictures is that possible thank you

Coding

```html
<!DOCTYPE html>
<html lang="en">
<head>
<meta charset="utf-8">
<title>Brightwell | Commercial Cleaning &amp; Maintenance</title>
<link href="https://fonts.googleapis.com/css2?family=Roboto:wght@300;400;500;700&display=swap" rel="stylesheet">
<style>
:root{
  --navy:#063a6e;
  --orange:#f6500c;
  --ink:#333333;
  --muted:#666666;
  --light:#f3f3f3;
  --footer:#2b2b2b;
  --footer-text:#9a9a9a;
  --white:#ffffff;
}
*{box-sizing:border-box;margin:0;padding:0}
html,body{width:1200px;height:3059px;overflow:hidden}
body{font-family:'Roboto',sans-serif;color:var(--ink);background:var(--white);position:relative}
section,header,footer{position:absolute;left:0;width:1200px}
.abs{position:absolute}
.btn{position:absolute;background:var(--orange);color:var(--white);font-weight:700;font-size:12px;letter-spacing:.6px;border-radius:20px;display:flex;align-items:center;justify-content:center;text-transform:uppercase;white-space:nowrap}

/* top bar */
.topbar{top:0;height:37px;background:var(--navy);color:var(--white);font-size:12px;font-weight:500}
.topbar .hours{left:66px;top:11px}
.topbar .contact{right:66px;top:11px;display:flex;gap:22px}
.topbar .contact span{display:flex;align-items:center;gap:5px}

/* nav */
.nav{top:37px;height:76px;background:var(--white);box-shadow:0 1px 3px rgba(0,0,0,.06)}
.brand{left:74px;top:19px;display:flex;align-items:center;gap:8px;font-size:30px;font-weight:400;color:var(--navy);letter-spacing:-.3px}
.brand .dot{width:28px;height:28px;border-radius:50%;background:var(--navy)}
.menu{right:72px;top:36px;display:flex;gap:30px;font-size:12px;font-weight:500;color:#333}
.menu span{display:flex;align-items:center;gap:8px}

/* hero */
.hero{top:113px;height:415px;background:linear-gradient(100deg,#5fa9c8 0%,#8cc3d6 30%,#c8d7d6 55%,#a9c6d0 75%,#6aaac2 100%)}
.hero h1{left:52px;top:126px;font-size:43px;font-weight:700;color:var(--white);letter-spacing:-1px}
.hero p{left:52px;top:203px;font-size:17px;color:var(--white)}
.hero .btn{left:52px;top:252px;width:113px;height:36px}

/* welcome */
.welcome{top:528px;height:546px}
.sec-title{left:0;width:1200px;text-align:center;font-size:38px;font-weight:500;letter-spacing:-.5px}
.sec-sub{left:0;width:1200px;text-align:center;font-size:15px;color:var(--muted)}
.o{color:var(--orange)}.n{color:var(--navy)}
.welcome .sec-title{top:72px;color:#333}
.welcome .sec-sub{top:126px}
.welcome .photo{left:113px;top:202px;width:234px;height:267px;background:linear-gradient(160deg,#7b7c78,#c9ccc9 45%,#a4a7a5 70%,#5f615e)}
.welcome .copy{left:431px;top:242px;width:695px;font-size:18px;line-height:28px;color:#555}
.welcome .copy b{font-weight:500;color:#444}

/* services */
.services{top:1074px;height:605px;background:var(--light)}
.services .sec-title{top:34px}
.services .sec-sub{top:88px}
.svc{position:absolute;width:330px}
.svc h3{font-size:22px;font-weight:500;color:#333;letter-spacing:-.3px;white-space:nowrap}
.svc p{font-size:13px;line-height:23px;color:var(--muted);margin-top:10px}
.svc.l{left:72px;text-align:right}
.svc.r{left:797px}
.svc .btn{position:relative;display:inline-flex;width:92px;height:27px;font-size:11px;margin-top:16px}
.svc .btn.wide{width:124px}
.circle{left:431px;top:200px;width:338px;height:338px;border-radius:50%;border:2px solid #aab9d0;padding:7px}
.circle div{width:100%;height:100%;border-radius:50%;border:1px solid #f3b59a;background:linear-gradient(180deg,#e9ecef 0%,#cdd8e4 40%,#4c7bb3 70%,#e4e6ea 100%)}

/* booking band */
.booking{top:1679px;height:151px;background:var(--navy);color:var(--white)}
.booking h2{left:66px;top:40px;font-size:29px;font-weight:700;letter-spacing:-.6px}
.booking p{left:66px;top:90px;font-size:14.5px}
.booking .btn{left:980px;top:56px;width:149px;height:57px;border-radius:29px;font-size:13px;letter-spacing:1px}

/* gallery */
.gallery{top:1830px;height:418px}
.gallery .sec-title{top:88px}
.thumbs{left:65px;top:190px;display:flex;gap:28px}
.thumb{width:155px;height:115px;background:linear-gradient(150deg,#4d5358,#b9bcbd 50%,#8b8f91)}
.thumb.b{background:linear-gradient(150deg,#2a8cc4 0%,#d8dde0 30%,#aeb3b6 70%,#333 100%)}
.dots{left:573px;top:347px;display:flex;gap:5px}
.dots i{width:13px;height:13px;border-radius:50%;background:var(--orange)}
.dots i:first-child{background:var(--navy)}

/* clients */
.clients{top:2248px;height:450px;background:var(--light)}
.clients .sec-title{top:93px}
.clients .sec-sub{top:145px;line-height:23px;width:700px;left:250px}
.logos{left:65px;top:245px;width:1070px;display:flex;justify-content:space-between;align-items:center}
.client{width:200px;height:96px;display:flex;align-items:center;justify-content:center;gap:8px;font-size:19px;font-weight:500;color:#555;text-align:center}
.client i{width:14px;height:14px;background:#555;flex:none}

/* footer */
.footer{top:2698px;height:361px;background:var(--footer);color:var(--footer-text)}
.col{position:absolute;top:50px}
.col h4{color:var(--white);font-size:20px;font-weight:500;letter-spacing:-.6px;padding-bottom:19px;border-bottom:1px solid #4a4a4a}
.col ul{list-style:none;margin-top:22px;font-size:14px}
.col li{height:32px;display:flex;align-items:flex-start;gap:14px}
.news{left:66px;width:338px}
.news p{font-size:14.5px;line-height:23px;margin-top:33px;width:330px}
.subscribe{display:flex;margin-top:25px;height:43px;border-radius:22px;overflow:hidden;background:#1c1c1c}
.subscribe span{flex:1;padding-left:12px;display:flex;align-items:center;font-size:13px;color:#aaa}
.subscribe b{width:111px;background:var(--orange);color:var(--white);font-size:12px;letter-spacing:.8px;display:flex;align-items:center;justify-content:center}
.links{left:431px;width:155px}
.social{left:614px;width:155px}
.social li i{width:9px;height:9px;background:#8a8a8a;display:inline-block;margin-top:4px;flex:none}
.company{left:797px;width:338px}
.company li{height:auto;margin-bottom:15px;line-height:22px}
.company svg{flex:none;margin-top:4px}
.copyright{left:66px;width:1068px;top:306px;border-top:1px solid #4a4a4a;padding-top:17px;text-align:center;font-size:10px;color:#aaa}
.copyright a{color:#2c8ae0;text-decoration:none}
</style>
</head>
<body>

<header class="topbar">
  <div class="abs hours">Mon to Fri: 8am - 5pm</div>
  <div class="abs contact">
    <span><svg width="11" height="11" viewBox="0 0 24 24"><path fill="#fff" d="M6.6 10.8a15 15 0 0 0 6.6 6.6l2.2-2.2a1 1 0 0 1 1-.25 11.4 11.4 0 0 0 3.6.57 1 1 0 0 1 1 1V20a1 1 0 0 1-1 1A17 17 0 0 1 3 4a1 1 0 0 1 1-1h3.5a1 1 0 0 1 1 1c0 1.250.2 2.450.57 3.57a1 1 0 0 1-.25 1z"/></svg>Call Now:(07) 3000 1234</span>
    <span><svg width="12" height="11" viewBox="0 0 24 20"><rect x="1" y="1" width="22" height="18" rx="3" fill="none" stroke="#fff" stroke-width="2"/><path d="M2 3l10 8 10-8" fill="none" stroke="#fff" stroke-width="2"/></svg>service@brightwellclean.com.au</span>
  </div>
</header>

<header class="nav">
  <div class="abs brand"><i class="dot"></i>Brightwell</div>
  <nav class="abs menu">
    <span>HOME</span>
    <span>ABOUT US <svg width="8" height="5" viewBox="0 0 8 5"><path d="M1 1l3 3 3-3" fill="none" stroke="#555" stroke-width="1.2"/></svg></span>
    <span>OUR TEAM</span>
    <span>SERVICES <svg width="8" height="5" viewBox="0 0 8 5"><path d="M1 1l3 3 3-3" fill="none" stroke="#555" stroke-width="1.2"/></svg></span>
    <span>SAFETY &amp; COMPLIANCE</span>
  </nav>
</header>

<section class="hero" role="img" aria-label="Rotating hero photo of a hand moving through clear blue water">
  <h1 class="abs">Quality Work With Affordable Price</h1>
  <p class="abs">We brings professional cleaning services right to your home.</p>
  <span class="btn">Read More</span>
</section>

<section class="welcome">
  <h2 class="abs sec-title">Welcome To <span class="o">Bright</span><span class="n">well</span></h2>
  <p class="abs sec-sub">A leading Australian cleaning services company.</p>
  <div class="abs photo" role="img" aria-label="Photo of a cleaned stainless steel double sink"></div>
  <p class="abs copy">When you work with <b>Brightwell</b> it is easy to do business with us.<br>Our people are professional, reliable and service oriented. In every interaction you have; on site, receiving help from our service support staff, or rolling-out new cleaning sites, you will see and feel the benefits of using Brightwell. The pride we take in our work and a prevailing focus on employees, customers and partners, delivers a consistent and superior ongoing service.</p>
</section>

<section class="services">
  <h2 class="abs sec-title"><span class="o">Our</span> <span class="n">Services</span></h2>
  <p class="abs sec-sub">Our focus on quality, our value add experience and professionalism.</p>

  <div class="svc l" style="top:201px">
    <h3>Equipment Cleaning &amp; Sanitising</h3>
    <p>Full cleaning, sanitisation and tune up service for food and commercial equipment.</p>
    <span class="btn">Read More</span>
  </div>
  <div class="svc l" style="top:378px">
    <h3>Pressure &amp; Playground Cleaning</h3>
    <p>High pressure gurney cleaning of hard surfaces and full playground equipment cleaning.</p>
    <span class="btn">Read More</span>
  </div>
  <div class="abs circle"><div role="img" aria-label="Photo of a team of cleaning staff in aprons with a cleaning trolley"></div></div>
  <div class="svc r" style="top:201px">
    <h3>General Cleaning &amp; Facilities</h3>
    <p>General commercial cleaning and property facilities management for every site.</p>
    <span class="btn">Read More</span>
  </div>
  <div class="svc r" style="top:378px">
    <h3>Project &amp; Recruiting Services</h3>
    <p>Cleaners, handymen, mechanics, warehousing staff and electricians can deposit a resume.</p>
    <span class="btn wide">Submit Resume</span>
  </div>
</section>

<section class="booking">
  <h2 class="abs">Book your appointment</h2>
  <p class="abs">Metropolitan Sydney, Brisbane, Melbourne, Adelaide, Newcastle and Regional areas as required.</p>
  <span class="btn">Get A Quote</span>
</section>

<section class="gallery">
  <h2 class="abs sec-title"><span class="o">Our</span> <span class="n">Gallery</span></h2>
  <div class="abs thumbs">
    <div class="thumb b" role="img" aria-label="Photo of cleaned drink dispenser"></div>
    <div class="thumb" role="img" aria-label="Photo of cleaned fryer station"></div>
    <div class="thumb" role="img" aria-label="Photo of cleaned stainless sink"></div>
    <div class="thumb b" role="img" aria-label="Photo of cleaned drink dispenser"></div>
    <div class="thumb" role="img" aria-label="Photo of cleaned fryer station"></div>
    <div class="thumb" role="img" aria-label="Photo of cleaned stainless sink"></div>
  </div>
  <div class="abs dots"><i></i><i></i><i></i></div>
</section>

<section class="clients">
  <h2 class="abs sec-title"><span class="o">Our</span> <span class="n">Clients</span></h2>
  <p class="abs sec-sub">Brightwell has established a strong reputation as being reliable, responsive and dedicated to fulfilling our customers and partners cleaning service needs.</p>
  <div class="abs logos">
    <div class="client"><i></i>Northgate Foods</div>
    <div class="client"><i></i>Maple Grill</div>
    <div class="client"><i></i>Coastline Beverages</div>
    <div class="client"><i></i>Burger Harbour</div>
    <div class="client"><i></i>R.T. Ashford</div>
  </div>
</section>

<footer class="footer">
  <div class="col news">
    <h4>Newsletters</h4>
    <p>Enter your email address to receive new information and other useful information right to your inbox.</p>
    <div class="subscribe"><span>Email Address</span><b>SUBSCRIBE</b></div>
  </div>
  <div class="col links">
    <h4>Quick Links</h4>
    <ul><li>About Us</li><li>Our Team</li><li>Services</li><li>Safety &amp; Compliance</li></ul>
  </div>
  <div class="col social">
    <h4>Social Feed</h4>
    <ul>
      <li><i></i>Pinewall</li><li><i></i>Chatterly</li><li><i></i>Orbit Plus</li><li><i></i>Careerlink</li><li><i></i>Streamview</li>
    </ul>
  </div>
  <div class="col company">
    <h4>Brightwell Pty.Ltd</h4>
    <ul>
      <li><svg width="12" height="14" viewBox="0 0 12 16"><path d="M6 0a6 6 0 0 0-6 6c0 4.5 6 10 6 10s6-5.5 6-10a6 6 0 0 0-6-6zm0 8.5A2.5 2.5 0 1 1 6 3.5a2.5 2.5 0 0 1 0 5z" fill="#8a8a8a"/></svg><span>Sydney | Brisbane | Melbourne | Adelaide<br>Australia ABN 41 555 208 117</span></li>
      <li><svg width="12" height="12" viewBox="0 0 24 24"><path fill="#8a8a8a" d="M6.6 10.8a15 15 0 0 0 6.6 6.6l2.2-2.2a1 1 0 0 1 1-.25 11.4 11.4 0 0 0 3.6.57 1 1 0 0 1 1 1V20a1 1 0 0 1-1 1A17 17 0 0 1 3 4a1 1 0 0 1 1-1h3.5a1 1 0 0 1 1 1c0 1.250.2 2.450.57 3.57a1 1 0 0 1-.25 1z"/></svg><span>Mobile: 0400 555 018</span></li>
      <li><svg width="13" height="12" viewBox="0 0 13 12"><rect x="0.5" y="2" width="12" height="9.5" rx="1" fill="none" stroke="#8a8a8a"/><rect x="3" y="0.5" width="7" height="3" fill="#8a8a8a"/></svg><span>Landline: 1300 555 210</span></li>
      <li><svg width="13" height="11" viewBox="0 0 24 20"><rect x="1" y="1" width="22" height="18" rx="2" fill="none" stroke="#8a8a8a" stroke-width="2"/><path d="M2 3l10 8 10-8" fill="none" stroke="#8a8a8a" stroke-width="2"/></svg><span>service@brightwellclean.com.au</span></li>
    </ul>
  </div>
  <div class="abs copyright">© 2020 <a>BRIGHTWELLCLEAN.COM</a> | ALL RIGHT RESERVED. DESIGNED BY <a>NORTHLANE STUDIO</a></div>
</footer>

</body>
</html>
```